BrightLane Real Estate Sign

We are in the process of rebranding our business and need a new For Sale \ Sold sign.
We're a prestige real estate agency and therefore require a really stylish sign.
I've uploaded the following files
1. The new company logo
2. "sample sign.jpg" which shows the type of sign we would like. It is a metal sign with a top panel and bottom panel.
3. Our previous sign "previous sign.jpg" if you're interested in seeing it.
The sign must be black with white text.
Our thoughts are that the top panel (refer to sample sign) would contain the text "For Sale" or "Sold". These would be two separate panels which are interchangeable and could be screwed in place.
The bottom panel would not contain any photos like the sample. However, it may contain our logo and my contact details etc.
The sign is 900mm wide x 1200mm high.
My details are:
Name: Desmond Harlow
Web: www.blrealestate.com.au
Email: sales@blrealestate.com.au
Phone: 0491 836 205

```html
<!DOCTYPE html>
<html lang="en">
<head>
<meta charset="utf-8">
<title>BrightLane Real Estate – Sold / For Sale Sign Panels</title>
<link rel="stylesheet" href="https://fonts.googleapis.com/css2?family=Cinzel:wght@700;900&family=Tinos:wght@700&display=swap">
<style>
  :root {
    --sign-black: #000000;
    --sign-white: #ffffff;
    --page-white: #ffffff;
    --contact-ink: #111111;
    --divider-grey: #8a8a8a;
  }
  * { margin: 0; padding: 0; box-sizing: border-box; }
  html, body {
    width: 1200px;
    height: 793px;
    overflow: hidden;
    background: var(--page-white);
  }
  .sign-set {
    position: relative;
    width: 1200px;
    height: 793px;
  }
  .sign-panel {
    position: absolute;
    top: 0;
    height: 793px;
    background: var(--sign-black);
    color: var(--sign-white);
  }
  .sign-panel--sold { left: 0; width: 595px; }
  .sign-panel--sale { left: 606px; width: 594px; }

  .headline {
    position: absolute;
    left: 0;
    right: 0;
    text-align: center;
    font-family: "Cinzel", "Times New Roman", serif;
    font-weight: 900;
    color: var(--sign-white);
    line-height: 1;
    letter-spacing: 6px;
  }
  .sign-panel--sold .headline {
    top: 140px;
    font-size: 166px;
  }
  .sign-panel--sale .headline {
    top: 35px;
    font-size: 166px;
    line-height: 205px;
  }
  .headline-line { display: block; }

  .brand {
    position: absolute;
    left: 26px;
    top: 612px;
    display: flex;
    align-items: center;
    gap: 12px;
  }
  .brand-square {
    width: 44px;
    height: 44px;
    background: var(--sign-white);
  }
  .brand-rule {
    width: 1px;
    height: 70px;
    background: var(--divider-grey);
  }
  .brand-name {
    font-family: "Tinos", "Times New Roman", serif;
    font-weight: 700;
    font-size: 30px;
    color: var(--sign-white);
    letter-spacing: 0.3px;
  }

  .contact-card {
    position: absolute;
    top: 568px;
    width: 293px;
    height: 177px;
    background: var(--sign-white);
    padding: 16px 0 0 8px;
    font-family: "Tinos", "Times New Roman", serif;
    font-weight: 700;
    font-size: 18px;
    color: var(--contact-ink);
    line-height: 40.5px;
    white-space: nowrap;
  }
  .sign-panel--sold .contact-card { left: 297px; }
  .sign-panel--sale .contact-card { left: 297px; }
  .contact-line { display: block; line-height: 40.5px; height: 40.5px; }
</style>
</head>
<body>
  <main class="sign-set">
    <section class="sign-panel sign-panel--sold" aria-label="Sold sign panel">
      <h1 class="headline"><span class="headline-line">SOLD</span></h1>
      <div class="brand">
        <span class="brand-square" aria-hidden="true"></span>
        <span class="brand-rule" aria-hidden="true"></span>
        <span class="brand-name">BrightLane</span>
      </div>
      <address class="contact-card" style="font-style:normal">
        <span class="contact-line">Contact : Desmond Harlow</span>
        <span class="contact-line">Phone: 0491 836 205</span>
        <span class="contact-line">Web: www.blrealestate.com.au</span>
        <span class="contact-line">Email: sales@blrealestate.com.au</span>
      </address>
    </section>

    <section class="sign-panel sign-panel--sale" aria-label="For sale sign panel">
      <h1 class="headline">
        <span class="headline-line">FOR</span>
        <span class="headline-line">SALE</span>
      </h1>
      <div class="brand">
        <span class="brand-square" aria-hidden="true"></span>
        <span class="brand-rule" aria-hidden="true"></span>
        <span class="brand-name">BrightLane</span>
      </div>
      <address class="contact-card" style="font-style:normal">
        <span class="contact-line">Contact : Desmond Harlow</span>
        <span class="contact-line">Phone: 0491 836 205</span>
        <span class="contact-line">Web: www.blrealestate.com.au</span>
        <span class="contact-line">Email: sales@blrealestate.com.au</span>
      </address>
    </section>
  </main>
</body>
</html>
```